Exciting letterhead design for startup company

We need a A4 letterhead designing.

See attached file which contains the logo (on 3 different coloured backgrounds) and then the address and contact information. It also contains 4 colours that can be used.

Looking for an imaginative design. We are a young, fresh startup website design company so need a letterhead that reflects our industry.

Font styles to use
Sans Serif

```html
<!DOCTYPE html>
<html lang="en">
<head>
<meta charset="utf-8">
<title>NetCrafted Letterhead</title>
<link href="https://fonts.googleapis.com/css2?family=Questrial&display=swap" rel="stylesheet">
<style>
  :root {
    --bg: #c9ccd0;
    --paper: #f2f2f2;
    --charcoal: #383b40;
    --amber: #f0b323;
    --blue: #3a8fd0;
    --ink: #4a4d52;
    --ink-dark: #2e3035;
  }
  * { margin: 0; padding: 0; box-sizing: border-box; }
  html, body { width: 1200px; height: 1000px; overflow: hidden; }
  body { background: var(--bg); font-family: "Questrial", "Century Gothic", sans-serif; color: var(--ink); position: relative; }
  .letterhead { position: absolute; left: 290px; top: 64px; width: 622px; height: 878px; background: var(--paper); box-shadow: 0 2px 6px rgba(0,0,0,.18); overflow: hidden; }
  .header { height: 87px; background: var(--charcoal); border-bottom: 4px solid var(--amber); position: relative; }
  .brand { position: absolute; left: 60px; top: 28px; font-size: 33px; color: #fff; letter-spacing: -0.5px; }
  .address { position: absolute; right: 57px; top: 34px; text-align: right; font-size: 9.5px; line-height: 10px; color: #e6e7e9; }
  .letter { position: absolute; left: 60px; top: 266px; width: 505px; font-size: 9.6px; line-height: 10.6px; }
  .salutation { font-weight: bold; color: var(--ink-dark); margin-bottom: 11px; }
  .letter p { text-align: justify; margin-bottom: 10.6px; }
  .closing { margin-top: 14px; position: relative; }
  .signer { font-weight: bold; color: var(--ink-dark); }
  .signature { position: absolute; left: 75px; top: -14px; width: 130px; height: 62px; background: linear-gradient(120deg, rgba(80,100,190,.25), rgba(80,100,190,.1)); border-radius: 4px; }
  .footer { position: absolute; left: 60px; right: 57px; top: 835px; display: flex; align-items: center; font-size: 9.2px; color: var(--ink); }
  .contact { display: flex; align-items: center; margin-right: 12px; }
  .icon { width: 9px; height: 9px; background: var(--blue); border-radius: 1.5px; margin-right: 5px; display: inline-flex; }
  .icon svg { width: 9px; height: 9px; }
  .website { margin-left: auto; }
  .website .accent { color: var(--blue); }
  .website .strong { color: var(--ink-dark); font-weight: bold; }
  .base-band { position: absolute; left: 0; bottom: 0; width: 622px; height: 14px; }
</style>
</head>
<body>
<main class="letterhead">
  <header class="header">
    <div class="brand">NetCrafted</div>
    <address class="address" style="font-style:normal">
      Suite 4, Meridian Court<br>
      Foundry Lane, Leeds<br>
      LS2 7QT, United Kingdom
    </address>
  </header>

  <section class="letter">
    <div class="salutation">Dear sir,</div>
    <p>Communication is a very integral part of living creatures, animals and humans. Communication may be verbal or written. Written communication however is only applicable to human beings. Can you even imagine a world without communication? Verbal communication can be through telephones, webcams or in person. Written communication is through letters, emails and mobile phone messages.</p>
    <p>In today’s world of great inventions and technology, letters have somehow become redundant. It is the time for text messages or chats. But they still can communicate a lot more than all other modes of communication. Organizations and various government departments still bank on letters as a strong medium of communication. There is no comparison in costs of sending letters as compared to costs of mobile phone messages though – letters are far cheaper. Letters now commonly known as “hard copy documents” are considered more relevant and important than email copies of text messages as proof or evidence of some sort.</p>
    <p>Letters speak volumes about a person or an organization that writes it. So one must take utmost care ensuring that the language used in any letter is appropriate for the occasion for which it is being written. Since a letter is also a written proof or document, if there are certain things that should not form a part of it, then that too should be carefully handled.</p>
    <p>Writing a good letter is an art. But if for some reason someone is unable to write that perfect letter, these different types of letters provide a base for you to build on. Sample letters have been given for everyone to understand what all information needs to form a part of the letter type and then it can be customized.</p>
    <div class="closing">
      <div>Yours Sincerely,</div>
      <div class="signer">Lena Morrow</div>
      <div class="signature" role="img" aria-label="Handwritten signature in blue ink"></div>
    </div>
  </section>

  <footer class="footer">
    <span class="contact"><span class="icon"><svg viewBox="0 0 9 9"><path d="M2.6 1.8c.3-.2.6 0 .8.3l.5.9c.1.3 0 .5-.2.7l-.4.3c.3.7.9 1.3 1.6 1.6l.3-.4c.2-.2.4-.3.7-.2l.9.5c.3.2.5.5.3.8l-.3.6c-.2.3-.6.4-1 .3C4.3 6.7 2.3 4.7 1.8 3c-.1-.4 0-.8.3-1z" fill="#fff"/></svg></span>0845 000 1234</span>
    <span class="contact"><span class="icon"><svg viewBox="0 0 9 9"><rect x="1.8" y="2.6" width="5.4" height="3.8" fill="none" stroke="#fff" stroke-width=".8"/><path d="M1.8 2.6l2.7 2 2.7-2" fill="none" stroke="#fff" stroke-width=".8"/></svg></span>hello@netcrafted.co.uk</span>
    <span class="contact"><span class="icon"></span>@netcrafted</span>
    <span class="website">www.<span class="strong">net</span><span class="accent strong">crafted</span>.co.uk</span>
  </footer>

  <svg class="base-band" viewBox="0 0 622 14" preserveAspectRatio="none" aria-hidden="true">
    <rect x="0" y="0" width="622" height="14" fill="#383b40"/>
    <polygon points="412,0 622,0 622,14 424,14" fill="#3a8fd0"/>
    <polygon points="405,0 412,0 424,14 417,14" fill="#2a2c30"/>
  </svg>
</main>
</body>
</html>
```